Finrazer 2014 Carp Fishing Tournament Presented by Corvale Fly Fishing

I need a promotional poster for a Carp fishing tournament that will take place in the Minneapolis/St.Paul area on June 21st 2014.
The tournament is open to anyone but it is fly fishing only. The cost to compete is $25 and proceeds will benefit Brook Keepers. It is a fun tournament with no cash prizes but there will be a raffle and prizes for biggest fish caught, ugliest fish caught, and most fish caught.
Corvale Fly Fishing Co. is my company and the poster should be branded with my logo and take inspiration from the overall feel of the brand but it doesn't have to be too similar. I'm definitely open to new designs and ideas. Here is a link to my website for review - www.corvaleflyfishing.example.
I'm not sure about the meeting place for the kickoff and award presentation but will have that nailed down very soon.

We will be adding sponsor logos to the bottom of the poster as we get them so there should be space for that somewhere if possible.
Our biggest supporter is Scalewise Magazine (logo attached) Their logo should be placed prominently on the poster but smaller than Corvale Fly Fishing.
Updates

I have now guaranteed payment for this project. 

Please read my brief more carefully and look at the example of the concert poster link i added to the brief.

For some reason my brief is not updating when I save and update so I'm going to write an update here and hopefully this will be seen by all designers.

I no longer want a homicide or need guns in the poster as stated previously in my " Nice to Have" section

- It would be great if we could have a carp actually committing a homicide on the poster. Possibly a carp with a gun shooting at another carp? or a fisherman getting shot by a carp?

we have desided that this is just to gnarly for the general public. Please let me know if you have any questions.

Target Market(s)

Think Skateboarding or old punk rock album covers like the Drabhounds, Grey Ruin, or the Welts, old concert posters are also something I like and can be used for inspiration
http://img-store-qx4.picboardly.example/236x/a1/22/9c/a1229c40d71f3b8e6a204c7dd8f51720.jpg

Industry/Entity Type

It Company

Requirements
Must have
• Must clearly show cost, and have Corvale Fly Fishing logo and Scalewise logos showing.
Nice to have
• It would be great if we could have a carp actually committing a homicide on the poster. Possibly a carp with a gun shooting at another carp? or a fisherman getting shot by a carp?
Should not have
• Should not have any pictures of someone fishing with a SPINNING ROD.

```html
<!DOCTYPE html>
<html lang="en">
<head>
<meta charset="utf-8">
<title>Finrazer 2014 Carp Fishing Tournament</title>
<link rel="stylesheet" href="https://fonts.googleapis.com/css2?family=Kaushan+Script&family=Arimo:wght@400;700&family=Oswald:wght@700&display=swap">
<style>
  :root {
    --page: #d9d4cc;
    --frame: #ffffff;
    --bg-light: #8c7760;
    --bg-mid: #5a4533;
    --bg-dark: #1f1610;
    --ink: #000000;
    --paper: #ffffff;
    --red: #e0202c;
    --ring-gold: #d49a45;
    --ring-dark: #6b3f17;
    --sponsor-orange: #f07a1c;
    --hunter-red: #d81f26;
  }
  html, body {
    margin: 0;
    width: 1000px;
    height: 1200px;
    overflow: hidden;
    background: var(--page);
  }
  .poster {
    position: absolute;
    left: 59px;
    top: 30px;
    width: 882px;
    height: 1140px;
    box-sizing: border-box;
    border: 6px solid var(--frame);
    border-radius: 8px;
    background: radial-gradient(ellipse at 50% 45%, var(--bg-light) 0%, var(--bg-mid) 50%, var(--bg-dark) 100%);
    overflow: hidden;
    font-family: "Arimo", Arial, sans-serif;
    color: var(--paper);
  }
  .crosshair { position: absolute; left: 0; top: 0; }
  .title {
    position: absolute;
    left: 0; right: 0; top: 44px;
    margin: 0;
    text-align: center;
    font-family: "Kaushan Script", cursive;
    font-weight: 400;
    font-size: 74px;
    line-height: 1;
  }
  .title .accent {
    color: var(--red);
    -webkit-text-stroke: 2px var(--paper);
    paint-order: stroke fill;
  }
  .title .rest {
    color: var(--paper);
    -webkit-text-stroke: 3px var(--ink);
    paint-order: stroke fill;
  }
  .when-where {
    position: absolute;
    left: 518px; width: 300px; top: 152px;
    margin: 0;
    text-align: center;
    font-size: 29px;
    line-height: 1.3;
  }
  .price {
    position: absolute;
    left: 24px; top: 226px;
    width: 200px;
  }
  .price .amount {
    display: inline-block;
    font-family: "Oswald", Impact, sans-serif;
    font-size: 86px;
    line-height: 1;
    color: var(--red);
    -webkit-text-stroke: 3px var(--paper);
    paint-order: stroke fill;
    letter-spacing: -2px;
  }
  .price .only {
    position: absolute;
    left: 138px; top: 14px;
    font-size: 24px;
    transform: rotate(90deg);
    transform-origin: left top;
    margin-left: 26px;
  }
  .price .label {
    margin: 4px 0 0;
    width: 150px;
    text-align: center;
    font-size: 25px;
    line-height: 1.35;
  }
  .scope-art {
    position: absolute;
    left: 175px; top: 263px;
    width: 538px; height: 538px;
    border-radius: 50%;
    background: radial-gradient(circle, #ffffff 0%, #f2f2f2 40%, #9a9a9a 80%, #111111 100%);
  }
  .badge {
    position: absolute;
    border-radius: 50%;
    background: var(--paper);
    display: flex;
    align-items: center;
    justify-content: center;
    text-align: center;
    font-weight: 700;
    line-height: 1.1;
  }
  .badge-host {
    left: 660px; top: 700px;
    width: 180px; height: 180px;
    color: var(--ink);
    font-size: 24px;
  }
  .badge-sponsor {
    left: 483px; top: 775px;
    width: 190px; height: 190px;
    color: var(--sponsor-orange);
    font-size: 28px;
  }
  .hunter-art {
    position: absolute;
    left: 10px; top: 922px;
    width: 164px; height: 164px;
    border-radius: 50%;
    background: radial-gradient(circle at 60% 85%, var(--hunter-red) 0%, var(--hunter-red) 25%, #f3f3f3 45%, #ffffff 100%);
  }
  .details {
    position: absolute;
    left: 186px; right: 8px; top: 976px;
    margin: 0;
    text-align: center;
    font-size: 16.5px;
    line-height: 1.3;
  }
  .site {
    position: absolute;
    left: 186px; right: 8px; top: 1070px;
    margin: 0;
    text-align: center;
    font-weight: 700;
    font-size: 33px;
    line-height: 1.2;
  }
</style>
</head>
<body>
<main class="poster">
  <svg class="crosshair" width="870" height="1128" viewBox="0 0 870 1128" aria-hidden="true">
    <defs>
      <radialGradient id="ring-fill" cx="50%" cy="50%" r="50%">
        <stop offset="88%" stop-color="var(--ring-dark)"/>
        <stop offset="94%" stop-color="var(--ring-gold)"/>
        <stop offset="100%" stop-color="var(--ring-dark)"/>
      </radialGradient>
    </defs>
    <line x1="444" y1="126" x2="444" y2="912" stroke="var(--ink)" stroke-width="9"/>
    <line x1="22" y1="532" x2="832" y2="532" stroke="var(--ink)" stroke-width="9"/>
    <circle cx="444" cy="532" r="288" fill="url(#ring-fill)" stroke="var(--ink)" stroke-width="14"/>
  </svg>
  <div class="scope-art" role="img" aria-label="Line illustration of a carp inside the scope sight"></div>

  <h1 class="title"><span class="accent">Carp Fishing</span> <span class="rest">Tournament</span></h1>
  <p class="when-where">Minneapolis/<br>St.Paul area on<br>June 21st 2014</p>

  <div class="price">
    <span class="amount">$25</span><span class="only">Only</span>
    <p class="label">Cost to Compete</p>
  </div>

  <div class="badge badge-host">Corvale</div>
  <div class="badge badge-sponsor">Scalewise</div>
  <div class="hunter-art" role="img" aria-label="Silhouette illustration of a hunter aiming a shotgun"></div>

  <p class="details">The tournament is open to anyone but it is fly fishing only.<br>The cost to compete is $25 and proceeds will benefit Brook Keepers. It is a fun tournament with no cash prizes but there will be a raffle and prizes for biggest fish caught, ugliest fish caught, and most fish caught.</p>
  <p class="site">www.corvaleflyfishing.example</p>
</main>
</body>
</html>
```